Modern Business Card for Lanternfield 2018

Our company assumes the best about people. We are creating an online community of entrepreneurs and business leaders who struggle with marketing their business online.

This business card should POP! We recently got a new logo and are launching a new website next month, so our business cards should make a statement that feels:
-Fresh
-Smart
-Trustworthy
-Fun

Target Market(s)

small business owners, entrepreneurs

Industry/Entity Type

Digital Marketing

Contact Information for Business Card

Dimensions: 3.5" x 2"

Font styles to use
Sans Serif

Colors
f37122
ffffff

Requirements
Must have
• We need a business card with a modern, bold design. We will use one side of the card as a lead-generation offer, so text on one side will need to fit up to 140 characters. The business card should stick to our core colors (orange, black, and white).
Nice to have
• We think a vertical "portrait" design could be interesting.
Should not have
• Should not look like a traditional business card. The round icon should stand out from a distance.

```html
<!DOCTYPE html>
<html lang="en">
<head>
<meta charset="utf-8">
<title>Lanternfield Business Card</title>
<link href="https://fonts.googleapis.com/css2?family=Josefin+Sans:wght@400;600;700&display=swap" rel="stylesheet">
<style>
  :root {
    --orange: #f37122;
    --ink: #231f20;
    --white: #ffffff;
    --stage: #3d4046;
  }
  * { margin: 0; padding: 0; box-sizing: border-box; }
  html, body { width: 1200px; height: 675px; overflow: hidden; }
  body {
    background: var(--stage);
    font-family: "Josefin Sans", sans-serif;
    display: flex;
    align-items: center;
    justify-content: center;
    gap: 80px;
  }
  .card {
    position: relative;
    width: 320px;
    height: 560px;
    background: var(--white);
    overflow: hidden;
  }
  .card-shapes { position: absolute; inset: 0; }
  .card-content { position: absolute; inset: 0; text-align: center; }

  /* Offer side */
  .headline {
    position: absolute; top: 70px; left: 0; right: 0;
    font-weight: 700; font-size: 21px; line-height: 1.12;
    color: var(--ink); letter-spacing: 0.2px;
  }
  .offer {
    position: absolute; top: 225px; left: 30px; right: 30px;
    font-size: 21px; line-height: 1.25; color: var(--ink);
  }
  .offer-url {
    display: block; margin-top: 16px;
    font-weight: 700; font-size: 19px;
  }
  .brand {
    position: absolute; top: 438px; left: 0; right: 0;
    display: flex; align-items: center; justify-content: center; gap: 10px;
  }
  .brand-dot {
    width: 34px; height: 34px; border-radius: 50%; background: var(--orange);
  }
  .brand-name {
    font-weight: 700; font-size: 30px; color: var(--ink); letter-spacing: 0.5px;
    text-transform: uppercase;
  }
  .tagline {
    position: absolute; top: 492px; left: 0; right: 0;
    font-size: 15px; font-weight: 600; color: var(--ink); letter-spacing: 0.5px;
  }

  /* Contact side */
  .role {
    position: absolute; top: 70px; left: 0; right: 0;
    font-size: 14px; color: var(--orange);
  }
  .person {
    position: absolute; top: 98px; left: 0; right: 0;
    font-size: 36px; font-weight: 400; color: var(--orange);
  }
  .email {
    position: absolute; top: 158px; left: 0; right: 0;
    font-size: 14px; color: var(--orange);
  }
  .mark {
    position: absolute; top: 360px; left: 0; right: 0;
    display: flex; flex-direction: column; align-items: center; gap: 16px;
  }
  .mark-circle {
    width: 110px; height: 110px; border-radius: 50%; background: var(--orange);
  }
  .mark-name {
    font-size: 24px; font-weight: 700; color: var(--orange); letter-spacing: 0.5px;
  }
</style>
</head>
<body>

  <section class="card card-offer">
    <svg class="card-shapes" viewBox="0 0 320 560" aria-hidden="true">
      <path fill="var(--orange)" d="M0 222 Q0 188 44 188 H276 Q320 188 320 150 V372 Q320 408 276 408 H44 Q0 408 0 446 Z"/>
    </svg>
    <div class="card-content">
      <p class="headline">REACH MORE PEOPLE.<br>MAKE MORE MONEY.<br>CREATE MORE IMPACT.</p>
      <p class="offer">Get your free Lanternfield Starter Package and our marketing guide today at
        <span class="offer-url">lanternfieldhq.com/start</span></p>
      <div class="brand">
        <span class="brand-dot"></span>
        <span class="brand-name">Lanternfield</span>
      </div>
      <p class="tagline">TELL STORIES THAT INSPIRE ACTION</p>
    </div>
  </section>

  <section class="card card-contact">
    <svg class="card-shapes" viewBox="0 0 320 560" aria-hidden="true">
      <path fill="var(--ink)" d="M0 0 H320 V200 Q300 300 0 300 Z"/>
    </svg>
    <div class="card-content">
      <p class="role">Story Marketing Coach</p>
      <h1 class="person">Mara Ellison</h1>
      <p class="email">mara@lanternfieldhq.com</p>
      <div class="mark">
        <span class="mark-circle"></span>
        <span class="mark-name">Lanternfield</span>
      </div>
    </div>
  </section>

</body>
</html>
```